Website page design

Hi, I need to improve the look of my homepage and the final offer page of my website. www.Pebble7dock.com We have an orvex buyback program where we purchase used orvex products from consumers nationwide. If you would go click through a sample offer on the site, you will the last view final offer page where we give you a cash offer for you site. I would like to keep the red and white colors since my logo is red and white. Please pay attention to the information shown on the homepage now, it is important for me to show the visitors this information on the home page. I would also love to give the users a friendly and inviting look when clicking on the options of orvex products on the home page.

Target Market(s)

Orvex electronics consumers

Number of Pages Required

2 page

Requirements
Nice to have
• On the final offer page, i would love for the offer to give an exciting look for the pebble 7 dock offer, and a boring look for the orvex buy back offer. At the final offer page you will my websites offer ( Your Pebble7dock Offer ) vs ( Orvex buyback program offer ) which is my competitor.

```html
<!DOCTYPE html>
<html lang="en">
<head>
<meta charset="utf-8">
<title>Pebble7dock – Homepage and Final Offer Page</title>
<link href="https://fonts.googleapis.com/css2?family=Figtree:wght@400;500;600;700&display=swap" rel="stylesheet">
<style>
:root{
  --red:#d0222a;
  --ink:#3d3d40;
  --muted:#8a8a8e;
  --light:#f7f7f8;
  --line:#e6e6e8;
  --dark:#2a2a2d;
  --darker:#1f1f21;
  --green:#2fb84f;
  --white:#fff;
}
*{box-sizing:border-box;margin:0;padding:0}
html,body{width:1033px;height:1200px;overflow:hidden;background:var(--white)}
body{font-family:"Figtree",sans-serif;color:var(--ink)}
.stage{position:absolute;left:0;top:0;width:1786px;height:2070px;transform:scale(0.5784);transform-origin:0 0}
.abs{position:absolute}
.caption{position:absolute;top:62px;font-size:18px;letter-spacing:1px;color:#666;text-align:center;width:755px}
.page{position:absolute;width:755px;overflow:hidden;background:var(--white);box-shadow:0 2px 14px rgba(0,0,0,.12)}
.home{left:98px;top:116px;height:1886px}
.offer{left:933px;top:116px;height:920px}
.brand{position:absolute;display:flex;align-items:center;gap:10px;font-weight:600;font-size:22px;white-space:nowrap}
.brand .dot{width:16px;height:16px;border-radius:50%;background:currentColor}
.nav{position:absolute;top:21px;left:265px;display:flex;gap:20px;font-size:11px;white-space:nowrap}
.btn{position:absolute;display:flex;align-items:center;justify-content:center;background:var(--red);color:var(--white);font-weight:600;border-radius:2px;white-space:nowrap}
.center{position:absolute;left:0;width:100%;text-align:center}
.title{font-size:26px;font-weight:500;line-height:32px;color:var(--ink)}
.title i{font-style:normal;color:var(--red)}
.hero{position:absolute;left:0;top:0;width:755px;height:394px;background:linear-gradient(135deg,#55565a 0%,#3a3b3f 45%,#2c2d30 100%);color:var(--white)}
.device{position:absolute;text-align:center;width:140px;font-size:14px}
.device .shot{width:110px;height:140px;margin:0 auto 14px;border-radius:8px;background:linear-gradient(160deg,#e9e9ec,#c9c9cf)}
.steps{position:absolute;left:18px;top:762px;width:719px;height:278px;background:var(--light)}
.step{position:absolute;top:108px;width:170px;text-align:center}
.step .icon{width:60px;height:60px;margin:0 auto 18px;border-radius:50%;background:#e3e3e6}
.step b{display:block;font-weight:500;font-size:13px;color:var(--ink)}
.step span{display:block;font-size:10px;color:var(--muted);margin-top:4px;line-height:14px}
.store{position:absolute;width:200px;text-align:center}
.store .name{height:84px;display:flex;align-items:center;justify-content:center;font-size:34px;font-weight:700;color:var(--ink);line-height:36px}
.store a{display:block;color:var(--red);font-size:13px;font-weight:500;margin-top:8px;text-decoration:none}
.footer{position:absolute;left:0;width:755px;height:199px;background:var(--dark);color:#d8d8da}
.footer .brand{left:57px;top:36px;color:var(--white)}
.footer .about{position:absolute;left:57px;top:80px;font-size:10px;line-height:15px;width:180px}
.fcol{position:absolute;top:40px;font-size:7.5px;line-height:20px;white-space:nowrap}
.fcol h4{font-size:7px;letter-spacing:1.5px;font-weight:700;color:var(--white);margin-bottom:4px;line-height:12px}
.fcol .addr{line-height:12px;margin-bottom:8px}
.fbot{position:absolute;top:178px;font-size:7px;white-space:nowrap}
.progress{position:absolute;left:0;top:60px;width:755px;height:110px;background:var(--light)}
.pstep{position:absolute;top:22px;width:100px;text-align:center}
.tick{width:22px;height:22px;border-radius:50%;background:var(--green);margin:0 auto 6px;display:flex;align-items:center;justify-content:center}
.pstep small{display:block;font-size:8px;color:var(--muted);letter-spacing:.3px}
.pstep span{display:block;font-size:10px;margin-top:8px;line-height:14px}
.card{position:absolute;background:var(--white)}
.card.main{left:104px;top:216px;width:245px;height:412px;box-shadow:0 4px 14px rgba(0,0,0,.14)}
.card.rival{left:472px;top:296px;width:178px;height:219px;background:var(--light)}
.card .head{height:100px;display:flex;align-items:center;justify-content:center;text-align:center;color:var(--white);font-weight:600;font-size:20px;line-height:25px}
.card.main .head{background:linear-gradient(135deg,#1fb3c9,#4fd3b0)}
.card.rival .head{height:81px;font-size:15px;line-height:20px;background:linear-gradient(135deg,#5a5a5e,#3b3b3f)}
.perk{position:absolute;left:21px;display:flex;align-items:center;gap:8px;font-size:10px;white-space:nowrap}
.con{position:absolute;left:15px;display:flex;align-items:center;gap:6px;font-size:7.5px;white-space:nowrap}
</style>
</head>
<body>
<div class="stage">
  <div class="caption" style="left:98px">THE HOMEPAGE</div>
  <div class="caption" style="left:933px">THE FINAL OFFER PAGE</div>

  <!-- Homepage -->
  <section class="page home">
    <div class="hero" role="img" aria-label="Dark photo of a laptop keyboard and phone on a desk">
      <div class="brand" style="left:45px;top:14px"><span class="dot"></span>Pebble7dock</div>
      <div class="nav" style="color:#e6e6e6"><span>How it Works?</span><span>Track My Order</span><span>FAQs</span></div>
      <div class="abs" style="left:558px;top:22px;font-size:11px;color:#ddd">Log In</div>
      <div class="btn" style="left:603px;top:15px;width:104px;height:26px;font-size:10px">Sell My Device</div>
      <div class="center" style="top:120px;font-size:30px;font-weight:600">We buy used orvex products<span style="color:var(--red)">.</span></div>
      <div class="center" style="top:180px;font-size:13.5px;line-height:19px">Fastest solution to your end of life orvex equipment,<br>start selling and get paid in 3 easy steps</div>
      <div class="btn" style="left:254px;top:250px;width:147px;height:36px;font-size:14px">Sell My Device</div>
      <div class="abs" style="left:422px;top:260px;font-size:13px;color:#ddd">Learn More ›</div>
    </div>

    <div class="center title" style="top:438px">Select your device to receive<br>an instant quote<i>.</i></div>
    <div class="device" style="left:59px;top:538px"><div class="shot" role="img" aria-label="Orvex Phone product photo"></div>Orvex Phone</div>
    <div class="device" style="left:225px;top:538px"><div class="shot" role="img" aria-label="Orvex Tab product photo"></div>Orvex Tab</div>
    <div class="device" style="left:390px;top:538px"><div class="shot" style="width:136px" role="img" aria-label="Orvex Book laptop product photo"></div>Orvex Book</div>
    <div class="device" style="left:556px;top:538px"><div class="shot" style="width:112px" role="img" aria-label="Orvex Desk computer product photo"></div>Orvex Desk</div>

    <div class="steps">
      <div class="center title" style="top:44px">How it works<i>.</i></div>
      <div class="step" style="left:65px"><div class="icon" role="img" aria-label="Offer document icon"></div><b>Get An Offer</b><span>Less than a minute</span></div>
      <div class="step" style="left:274px"><div class="icon" role="img" aria-label="Free delivery stamp icon"></div><b>Ship It Free</b><span>We provide a pre-paid</span></div>
      <div class="step" style="left:490px"><div class="icon" role="img" aria-label="Piggy bank icon"></div><b>Get Paid Fast</b><span>Payvine, check or bank<br>transfer</span></div>
    </div>

    <div class="center title" style="top:1084px">We sell good-quality used orvex<br>products at fair price<i>.</i></div>
    <div class="store" style="left:117px;top:1178px"><div class="name">Marlo<br>Renewed</div><a>Visit Store ›</a></div>
    <div class="store" style="left:437px;top:1178px"><div class="name">Bidnest</div><a>Visit Store ›</a></div>

    <div class="abs" style="left:0;top:1328px;width:755px;height:1px;background:var(--line)"></div>
    <div class="center title" style="top:1374px">Loved by thousands of clients<i>.</i></div>
    <div class="abs" style="left:328px;top:1440px;width:88px;height:40px;background:var(--green);border-radius:3px" role="img" aria-label="Review platform rating badge"></div>
    <div class="center" style="top:1504px;font-size:10px;line-height:15px;color:#666">" Integre principes vim ad, est te partem imperdiet vituperatoribus.<br>Dicit tincidunt comprehensam ne qui. In alterum alienum mediocrem est, eum ut commune mentitum "</div>
    <div class="center" style="top:1541px;font-size:6px;color:var(--red)">BY JORDAN LEE</div>
    <div class="center" style="top:1574px;display:flex;justify-content:center;gap:5px">
      <span style="width:6px;height:6px;border-radius:50%;background:var(--red)"></span>
      <span style="width:4px;height:4px;margin-top:1px;border-radius:50%;background:#ccc"></span>
      <span style="width:4px;height:4px;margin-top:1px;border-radius:50%;background:#ccc"></span>
    </div>
    <div class="btn" style="left:258px;top:1607px;width:105px;height:26px;font-size:10.5px">Sell My Device</div>
    <div class="abs" style="left:387px;top:1613px;font-size:10.5px;color:var(--muted)">View More Reviews ›</div>

    <footer class="footer" style="top:1688px">
      <div class="brand"><span class="dot"></span>Pebble7dock</div>
      <p class="about">We offers companies and individuals the fastest solution to their end of life orvex equipment.</p>
      <div class="fcol" style="left:369px"><h4>GET IN TOUCH</h4><div class="addr">48 Larkspur Lane<br>Millbrook, NY, 10990</div>555-014-2273</div>
      <div class="fcol" style="left:520px"><h4>LEARN MORE</h4>About Us<br>How it Works?<br>Track My Order<br>FAQs<br>Contact Us</div>
      <div class="fcol" style="left:646px"><h4>FOLLOW US</h4>▪ Chatter<br>▪ Snapline</div>
      <div class="fbot" style="left:57px">© 2019 By Pebble7dock. All rights reserved.</div>
      <div class="fbot" style="left:602px">Privacy Policy &nbsp;&nbsp; Terms of Use</div>
    </footer>
  </section>

  <!-- Final offer page -->
  <section class="page offer">
    <div class="abs" style="left:0;top:0;width:755px;height:60px;background:var(--darker)">
      <div class="brand" style="left:45px;top:17px;color:var(--red)"><span class="dot"></span>Pebble7dock</div>
      <div class="nav" style="color:#e6e6e6;top:24px"><span>How it Works?</span><span>Track My Order</span><span>FAQs</span></div>
      <div class="abs" style="left:558px;top:23px;font-size:11px;color:#ddd">Log In</div>
      <div class="btn" style="left:603px;top:16px;width:104px;height:26px;font-size:10px;background:none;border:1.5px solid #fff">Sell My Device</div>
    </div>

    <div class="progress">
      <div class="abs" style="left:75px;top:33px;width:603px;height:1px;background:var(--line)"></div>
      <div class="pstep" style="left:25px"><div class="tick"><svg width="11" height="9" viewBox="0 0 11 9"><path d="M1 4.5 4 7.5 10 1" stroke="#fff" stroke-width="2" fill="none"/></svg></div><small>DEVICE</small><span>Orvex Book</span></div>
      <div class="pstep" style="left:126px"><div class="tick"><svg width="11" height="9" viewBox="0 0 11 9"><path d="M1 4.5 4 7.5 10 1" stroke="#fff" stroke-width="2" fill="none"/></svg></div><small>MODEL</small><span>17" Pro</span></div>
      <div class="pstep" style="left:226px"><div class="tick"><svg width="11" height="9" viewBox="0 0 11 9"><path d="M1 4.5 4 7.5 10 1" stroke="#fff" stroke-width="2" fill="none"/></svg></div><small>PROCESSOR</small><span>3.06 GHz Dual-Core<br>(2009)</span></div>
      <div class="pstep" style="left:327px"><div class="tick"><svg width="11" height="9" viewBox="0 0 11 9"><path d="M1 4.5 4 7.5 10 1" stroke="#fff" stroke-width="2" fill="none"/></svg></div><small>HARD DRIVE</small><span>500 GB</span></div>
      <div class="pstep" style="left:427px"><div class="tick"><svg width="11" height="9" viewBox="0 0 11 9"><path d="M1 4.5 4 7.5 10 1" stroke="#fff" stroke-width="2" fill="none"/></svg></div><small>MEMORY</small><span>4 GB</span></div>
      <div class="pstep" style="left:528px"><div class="tick"><svg width="11" height="9" viewBox="0 0 11 9"><path d="M1 4.5 4 7.5 10 1" stroke="#fff" stroke-width="2" fill="none"/></svg></div><small>ACCESSORIES</small><span>1</span></div>
      <div class="pstep" style="left:628px"><div class="tick"><svg width="11" height="9" viewBox="0 0 11 9"><path d="M1 4.5 4 7.5 10 1" stroke="#fff" stroke-width="2" fill="none"/></svg></div><small>CONDITION</small><span>Normal</span></div>
    </div>

    <div class="card main">
      <div class="head" role="img" aria-label="Teal tinted photo of a laptop keyboard">Your Pebble7dock<br>Offer</div>
      <div class="perk" style="top:128px"><svg width="13" height="13" viewBox="0 0 13 13"><circle cx="6.5" cy="6.5" r="5.5" stroke="var(--green)" fill="none" stroke-width="1.2"/><path d="M3.8 6.6 5.8 8.5 9.3 4.6" stroke="var(--green)" fill="none" stroke-width="1.2"/></svg>Lorem ipsum dolor sit amet consect</div>
      <div class="perk" style="top:159px"><svg width="13" height="13" viewBox="0 0 13 13"><circle cx="6.5" cy="6.5" r="5.5" stroke="var(--green)" fill="none" stroke-width="1.2"/><path d="M3.8 6.6 5.8 8.5 9.3 4.6" stroke="var(--green)" fill="none" stroke-width="1.2"/></svg>Praesent sit amet magna ut est</div>
      <div class="perk" style="top:191px"><svg width="13" height="13" viewBox="0 0 13 13"><circle cx="6.5" cy="6.5" r="5.5" stroke="var(--green)" fill="none" stroke-width="1.2"/><path d="M3.8 6.6 5.8 8.5 9.3 4.6" stroke="var(--green)" fill="none" stroke-width="1.2"/></svg>Donec at mauris eu nibh lobortis</div>
      <div class="perk" style="top:222px"><svg width="13" height="13" viewBox="0 0 13 13"><circle cx="6.5" cy="6.5" r="5.5" stroke="var(--green)" fill="none" stroke-width="1.2"/><path d="M3.8 6.6 5.8 8.5 9.3 4.6" stroke="var(--green)" fill="none" stroke-width="1.2"/></svg>Phasellus at faucibus ipsum</div>
      <div class="abs" style="left:0;top:266px;width:245px;height:1px;background:var(--line)"></div>
      <div class="center" style="top:280px;display:flex;justify-content:center;align-items:center;gap:10px">
        <s style="font-size:9px;color:#aaa">$150</s><span style="font-size:34px;font-weight:500">$201</span>
      </div>
      <div class="btn" style="left:45px;top:330px;width:155px;height:38px;font-size:15px">Sell Now!</div>
      <div class="center" style="top:378px;font-size:9.5px;color:#aaa">Offer valid for 30 days</div>
    </div>

    <div class="abs" style="left:390px;top:386px;font-size:30px;font-weight:600">vs<span style="color:var(--red)">.</span></div>

    <div class="card rival">
      <div class="head" role="img" aria-label="Dark photo of a pile of used phones">Orvex Buyback<br>Program Offer</div>
      <div class="con" style="top:104px"><svg width="8" height="8" viewBox="0 0 8 8"><path d="M1 1 7 7M7 1 1 7" stroke="var(--red)" stroke-width="1.2"/></svg>Lorem ipsum dolor sit amet conset</div>
      <div class="con" style="top:127px"><svg width="8" height="8" viewBox="0 0 8 8"><path d="M1 1 7 7M7 1 1 7" stroke="var(--red)" stroke-width="1.2"/></svg>Aenean varius nisl sed orci gravida</div>
      <div class="con" style="top:149px"><svg width="8" height="8" viewBox="0 0 8 8"><path d="M1 1 7 7M7 1 1 7" stroke="var(--red)" stroke-width="1.2"/></svg>Nunc blandit sollicitudin velit</div>
      <div class="center" style="top:172px;font-size:24px;font-weight:500">$201</div>
    </div>

    <footer class="footer" style="top:721px">
      <div class="brand"><span class="dot"></span>Pebble7dock</div>
      <p class="about">We offers companies and individuals the fastest solution to their end of life orvex equipment.</p>
      <div class="fcol" style="left:369px"><h4>GET IN TOUCH</h4><div class="addr">48 Larkspur Lane<br>Millbrook, NY, 10990</div>555-014-2273</div>
      <div class="fcol" style="left:520px"><h4>LEARN MORE</h4>About Us<br>How it Works?<br>Track My Order<br>FAQs<br>Contact Us</div>
      <div class="fcol" style="left:646px"><h4>FOLLOW US</h4>▪ Chatter<br>▪ Snapline</div>
      <div class="fbot" style="left:57px">© 2019 By Pebble7dock. All rights reserved.</div>
      <div class="fbot" style="left:602px">Privacy Policy &nbsp;&nbsp; Terms of Use</div>
    </footer>
  </section>
</div>
</body>
</html>
```